**** Web design project for VornaSoft ****

For my ICT company VornaSoft I need a website.

We design, build and host web-applications and we have our own CMS product. In the references part we want to show sample websites (thumbnails) + links.

It should look modern (WEB 2.0), rounded corners.

I want the following menu' s:
- Home
- Services
- References
- News
- About VornaSoft
- Contact

Sample websites:
See attachments
http://www.plumvest.com
http://www.gadomirbureauwerk.nl

Reason: Want to take some time for feedback and improvements.

Reason: I'm waiting for a black background, with shadow and ambient light. You'll make a good chance!

Industry/Entity Type

It Company

Requirements
Must have
• - Fixed width (1024px), should fit on an IPad2
- Language selection English/Dutch
- Chirpline/Friendwall/Worknet/RSS icons
- Footer for Terms of use and Copyrights
- Search box
- 3 (or more) boxes for information i.e. news, blog or advertisements
Nice to have
• - Footer Site Map
- Contrasting background outside borders
- wide image (rotator) (with transperant sentence block)
- Shadow

```html
<!DOCTYPE html>
<html lang="en">
<head>
<meta charset="utf-8">
<title>VornaSoft – Home</title>
<link href="https://fonts.googleapis.com/css2?family=Arimo:wght@400;700&family=Quicksand:wght@500&family=Tinos&display=swap" rel="stylesheet">
<style>
:root{
  --header:#1f2a2b;
  --page:#f1ecd6;
  --footer:#f2e9c8;
  --blue:#1b9ad2;
  --blue-light:#33c1ee;
  --blue-dark:#0d7fb5;
  --green:#8cc63f;
  --green-dark:#5e9a17;
  --body:#333;
  --line:#d9d9d9;
}
*{margin:0;padding:0;box-sizing:border-box}
html,body{width:803px;height:1200px;overflow:hidden}
body{position:relative;background:var(--page);font-family:Arimo,Arial,sans-serif;color:var(--body)}
.abs{position:absolute}
.site-header{left:0;top:0;width:803px;height:163px;background:var(--header)}
.brand{left:52px;top:22px;display:flex;align-items:center;gap:14px}
.brand-mark{width:76px;height:76px;border-radius:50%;background:var(--blue)}
.brand-name{font-size:40px;color:#b9c3c7;letter-spacing:.5px}
.lang{top:8px;width:26px;height:18px;border:1px solid #fff}
.lang-en{left:703px;background:#2b3f8c}
.lang-nl{left:732px;background:linear-gradient(#c8102e 0 33%,#fff 33% 66%,#21468b 66%)}
.search{left:555px;top:61px;width:168px;height:20px;background:#fff;border-radius:10px 0 0 10px;font-size:8px;color:#999;padding:6px 0 0 22px}
.search-icon{left:561px;top:66px;width:9px;height:9px;border:1.5px solid #888;border-radius:50%}
.search-btn{left:721px;top:61px;width:42px;height:20px;background:linear-gradient(var(--green),var(--green-dark));border-radius:0 6px 6px 0;font-size:9px;color:#143;text-align:center;line-height:20px}
.main-nav{left:40px;top:117px;width:728px;height:35px;border-radius:6px;background:linear-gradient(var(--blue-light),var(--blue-dark));display:flex;overflow:hidden}
.main-nav a{color:#fff;text-decoration:none;font-size:10px;text-align:center;line-height:35px;border-right:1px solid rgba(255,255,255,.3)}
.main-nav a.active{background:linear-gradient(#9cd44a,var(--green-dark))}
.slider{left:40px;top:179px;width:729px;height:239px;border-radius:10px;border:2px solid #fff;box-shadow:0 0 6px rgba(0,0,0,.25);overflow:hidden;background:linear-gradient(100deg,#fff 0%,#eef3f6 45%,#aec7d8 70%,#5a6f82 100%)}
.slider-title{left:25px;top:160px;font-family:Quicksand,sans-serif;font-size:32px;color:var(--blue)}
.slider-arrow{top:115px;width:22px;height:22px;border-radius:50%;background:#222;border:2px solid #ccc}
.panel{background:#fff;border-radius:10px;box-shadow:0 0 6px rgba(0,0,0,.18)}
.panel-tab{position:absolute;left:-4px;top:10px;height:26px;padding:0 26px 0 12px;background:linear-gradient(var(--blue-light),var(--blue));clip-path:polygon(0 0,100% 0,88% 100%,0 100%);font-family:Tinos,serif;font-size:14px;color:#fff;line-height:26px}
.copy{font-size:8.6px;line-height:13px;color:#1f6da8}
.more{font-size:8px;color:#1f4f86}
.side h3{font-size:10.5px;font-weight:400;color:var(--blue);border-bottom:1px solid var(--line);padding-bottom:4px;margin-bottom:6px}
.side h4{font-size:8.6px;color:var(--blue-dark);margin-bottom:3px}
.side p{font-size:8.6px;line-height:12px;color:var(--blue);margin-bottom:6px}
.thumb{top:48px;width:102px;height:113px;border:1px solid #ccc;border-radius:4px}
.cms-arrow{top:92px;width:16px;height:18px;background:#bbb}
.ad{top:943px;width:341px;height:43px;background:linear-gradient(90deg,#6b8f3b,#a5c26a 70%,#e8eadf);font-family:Tinos,serif;color:#fff;padding:6px 0 0 20px;font-size:18px}
.ad small{display:block;font-family:Arimo,Arial,sans-serif;font-size:8px}
.site-footer{left:0;top:1023px;width:803px;height:177px;background:var(--footer)}
.fcol{top:1052px;font-size:8px;line-height:13.2px;color:#222}
.fcol h5{font-size:10px;font-weight:400;margin-bottom:6px}
.social li{list-style:none;display:flex;align-items:center;gap:6px;margin-bottom:6px}
.social i{width:11px;height:11px;background:var(--blue);display:inline-block}
.map{left:518px;top:1051px;width:99px;height:93px;background:#e1ddd2;border:1px solid #aaa}
.office{left:629px;top:1052px;font-size:8.4px;line-height:13.2px;color:#555;font-style:normal}
.office b{color:#333}
.legal{left:0;top:1169px;width:803px;border-top:1px solid #d8cfa8;text-align:center;font-size:8px;padding-top:9px;color:#333}
</style>
</head>
<body>
<header class="site-header abs">
  <div class="brand abs"><span class="brand-mark"></span><span class="brand-name">VornaSoft</span></div>
  <span class="lang lang-en abs" aria-label="English"></span>
  <span class="lang lang-nl abs" aria-label="Nederlands"></span>
  <div class="search abs">Enter Search Here</div>
  <span class="search-icon abs"></span>
  <div class="search-btn abs">Search</div>
  <nav class="main-nav abs">
    <a class="active" style="width:92px">HOME</a>
    <a style="width:121px">SERVICES</a>
    <a style="width:137px">REFERENCES</a>
    <a style="width:107px">NEWS</a>
    <a style="width:155px">ABOUT VORNASOFT</a>
    <a style="width:116px;border:0">CONTACT</a>
  </nav>
</header>

<section class="slider abs" role="img" aria-label="Hero photo of a businessman with a tablet in a bright office">
  <span class="slider-arrow abs" style="left:4px"></span>
  <span class="slider-arrow abs" style="left:689px"></span>
  <div class="slider-title abs">Lorel Ipsum Dolor Sit amet</div>
</section>

<section class="panel abs" style="left:44px;top:442px;width:509px;height:264px">
  <div class="panel-tab">Welcome To VORNASOFT</div>
  <div class="abs copy" style="left:13px;top:45px;width:310px">
    <p>Lorem ipsum dolor sit amet, consectetur adipiscing elit. Integer porttitor nisi cursus nulla ornare et lacinia risus iaculis. Proin rhoncus ante quis mi interdum non auctor orci malesuada.Lorem ipsum dolor sit amet, consectetur adipiscing elit. Integer porttitor nisi cursus nulla ornare et lacinia risus iaculis. Proin rhoncus ante quis mi interdum non auctor orci malesuada Lorem ipsum dolor sit amet, consectetur adipiscing elit. Integer porttitor nisi cursus nulla ornare et lacinia risus iaculis. Proin rhoncus ante quis mi interdum non auctor orci malesuada.</p><br>
    <p>Lorem ipsum dolor sit amet, consectetur adipiscing elit. Integer porttitor nisi cursus nulla ornare et lacinia risus iaculis. Proin rhoncus ante quis mi interdum non auctor orci malesuada.Lorem ipsum dolor sit amet, consectetur</p>
  </div>
  <div class="abs" role="img" aria-label="Photo of two business colleagues at a laptop" style="left:338px;top:45px;width:160px;height:155px;border-radius:8px;border:1px solid #ccc;background:linear-gradient(#eef1f3,#b9c3cc)"></div>
  <div class="abs more" style="left:13px;top:232px">» Read More</div>
</section>

<aside class="panel side abs" style="left:567px;top:442px;width:201px;height:185px">
  <div class="panel-tab">Latest Blog</div>
  <div class="abs" style="left:9px;top:40px;width:183px">
    <h3>Lorel Ipsum dolor sit amet</h3><h4>Posted on 14-04-2012</h4><p>Lorem ipsum dolor sit amet, consectetur adipiscing elit.</p>
    <h3>Lorel Ipsum dolor sit amet</h3><h4>Posted on 14-04-2012</h4><p>Lorem ipsum dolor sit amet, consectetur adipiscing elit.</p>
    <div class="more" style="text-align:right;font-weight:700">More Blog Post</div>
  </div>
</aside>

<aside class="panel side abs" style="left:567px;top:644px;width:201px;height:263px">
  <div class="panel-tab">Latest News</div>
  <div class="abs" style="left:9px;top:43px;width:183px">
    <h3>Lorel Ipsum dolor sit amet</h3><h4>Posted on 14-04-2012</h4><p>Lorem ipsum dolor sit amet, consectetur adipiscing elit. Integer porttitor nisi cursus nulla ornare et lacinia risus iaculis. Proin</p><div class="more" style="margin-bottom:10px">» Read More</div>
    <h3>Lorel Ipsum dolor sit amet</h3><h4>Posted on 14-04-2012</h4><p>Lorem ipsum dolor sit amet, consectetur adipiscing elit. Integer porttitor nisi cursus nulla ornare et lacinia risus iaculis. Proin</p><div class="more">» Read More</div>
  </div>
</aside>

<section class="panel abs" style="left:44px;top:725px;width:509px;height:182px">
  <div class="panel-tab">Sample CMS</div>
  <span class="cms-arrow abs" style="left:10px"></span>
  <div class="thumb abs" role="img" aria-label="Sample website thumbnail with blue header" style="left:40px;background:linear-gradient(#f4f7fa 25%,#4a6f98 25%)"></div>
  <div class="thumb abs" role="img" aria-label="Sample website thumbnail with dark space image" style="left:150px;background:linear-gradient(#fff 30%,#2d3b5a 30%)"></div>
  <div class="thumb abs" role="img" aria-label="Sample website thumbnail with teal banner" style="left:261px;background:linear-gradient(#dfe8ea 10%,#1f6c7d 10% 70%,#e6ece8 70%)"></div>
  <div class="thumb abs" role="img" aria-label="Sample website thumbnail with red layout" style="left:371px;background:linear-gradient(#c72d2a 20%,#f4f0ee 20%)"></div>
  <span class="cms-arrow abs" style="left:482px"></span>
</section>

<div class="ad abs" style="left:63px">WanderPaws.net<small>Travel gear and accessories for your dog.</small></div>
<div class="ad abs" style="left:412px">WanderPaws.net<small>Travel gear and accessories for your dog.</small></div>

<footer class="site-footer abs"></footer>
<div class="fcol abs" style="left:53px"><h5>About Us</h5>Dummy Link<br>Dummy Link<br>Dummy Link<br>Dummy Link<br>Dummy Link<br>Dummy Link</div>
<div class="fcol abs" style="left:159px"><h5>Smaple Links</h5>Dummy Link<br>Dummy Link<br>Dummy Link<br>Dummy Link<br>Dummy Link<br>Dummy Link</div>
<div class="fcol abs" style="left:270px"><h5>Sample Links</h5>Dummy Link<br>Dummy Link<br>Dummy Link</div>
<div class="fcol abs" style="left:399px"><h5>Get in Touch</h5>
  <ul class="social"><li><i></i>Friendwall</li><li><i></i>Chirpline</li><li><i></i>Clipstream</li><li><i></i>Worknet</li><li><i style="background:#e8782a"></i>Rss</li></ul>
</div>
<div class="map abs" role="img" aria-label="Small street map showing the head office location"></div>
<address class="office abs"><b>VORNASOFT HEAD OFFICE</b><br>P-14 Block-C, Eastfield<br>Lindmoor 700120<br>Phone No. (31)2048-5521<br>Email: admin@vornasoft.com<br>Fax : (31) 2048 - 5530<br><span style="color:#222">Contact Us »</span></address>
<div class="legal abs">© 2012, All Rights Reserved, vornasoft.com</div>
</body>
</html>
```